Melva's 40th Invitation

I need an invitation designed for a 40th birthday in Singapore. The theme is a "long lunch", set in a colonial garden (black and white house - Singapore style if you want to Google or Bing it).
Look and feel should be simple, elegant, stylish, bold, fresh, minimalist. Nothing fussy, intricate, formal or too colourful. No intials, not wedding-like, minimal colour (no golds).
Setting will be garden setting with champagne, white marquee, white table cloths, long trestle tables, fresh white floowers (lilys or hydrangas).
Format should be PC friendly (jpeg, gif, pdf etc).
Size is flexible to accomodate design - it will be emailed as an attachment.
Details to include:
- Saturday, 27th November, 2010
Time - From 1pm.
Address - 27 Quenby Rise, Singapore
Dress: Garden Glam
RSVP - tolvane@pexorin.com by 13 November, 2010

```html
<!DOCTYPE html>
<html lang="en">
<head>
<meta charset="utf-8">
<title>Melva's 40th – Invitation</title>
<link rel="stylesheet" href="https://fonts.googleapis.com/css2?family=Cinzel+Decorative:wght@400;700&family=Pinyon+Script&display=swap">
<style>
  :root {
    --frame-dark: #151a19;
    --frame-mid: #3c4a48;
    --frame-light: #8fa5a1;
    --silk-deep: #6f9e98;
    --silk-mid: #a9d3cc;
    --silk-light: #e4f5f1;
    --ink: #1c1614;
    --glow: rgba(255, 255, 255, 0.85);
    --ornament-tile: #1e2524;
    --ornament-tone: #9fc7c0;
    --flourish-tone: #241c1a;
  }
  html, body {
    margin: 0;
    padding: 0;
    width: 1200px;
    height: 514px;
    overflow: hidden;
    background: #ffffff;
  }
  .invitation {
    position: relative;
    width: 1200px;
    height: 514px;
    box-sizing: border-box;
    border: 17px solid var(--frame-dark);
    border-image: linear-gradient(135deg, var(--frame-dark), var(--frame-mid) 30%, var(--frame-light) 50%, var(--frame-mid) 70%, var(--frame-dark)) 1;
    background:
      linear-gradient(100deg, transparent 0 18%, rgba(255,255,255,0.35) 24%, transparent 30% 48%, rgba(255,255,255,0.4) 54%, transparent 60% 74%, rgba(255,255,255,0.35) 80%, transparent 86%),
      linear-gradient(75deg, var(--silk-deep), var(--silk-mid) 25%, var(--silk-light) 45%, var(--silk-mid) 65%, var(--silk-deep) 85%, var(--silk-mid));
    box-shadow: inset 0 0 40px rgba(20, 40, 38, 0.55);
    overflow: hidden;
  }
  .corner-ornament {
    position: absolute;
    left: 0;
    top: 0;
    width: 86px;
    height: 86px;
    background: radial-gradient(circle, var(--ornament-tone) 0 35%, var(--ornament-tile) 75%);
    border: 2px solid var(--frame-light);
    box-sizing: border-box;
  }
  .title {
    position: absolute;
    left: 250px;
    top: 6px;
    width: 880px;
    margin: 0;
    text-align: center;
    font-family: "Cinzel Decorative", serif;
    font-weight: 400;
    font-size: 44px;
    letter-spacing: 3px;
    color: var(--ink);
    text-shadow: 0 0 4px var(--glow), 0 0 8px var(--glow);
  }
  .details {
    position: absolute;
    left: 130px;
    top: 82px;
    width: 900px;
    text-align: center;
    font-family: "Pinyon Script", cursive;
    font-size: 36px;
    line-height: 44px;
    color: var(--ink);
    text-shadow: 0 0 4px var(--glow), 0 0 8px var(--glow);
  }
  .details p { margin: 0; }
  .details .time { margin-bottom: 58px; }
  .flourish {
    position: absolute;
    left: 420px;
    top: 386px;
    width: 336px;
    height: 86px;
    background: radial-gradient(ellipse at center, var(--flourish-tone) 0 30%, rgba(36,28,26,0.35) 60%, transparent 72%);
  }
</style>
</head>
<body>
  <main class="invitation">
    <div class="corner-ornament" role="img" aria-label="Square leaf and knotwork ornament tile"></div>
    <h1 class="title">You are Cordially Invited</h1>
    <section class="details">
      <p class="date">Saturday November 27, 2010</p>
      <p class="time">1 pm</p>
      <p class="address">Address - 27 Quenby Rise, Singapore</p>
      <p class="dress">Dress: Garden Glam</p>
      <p class="rsvp">RSVP - tolvane@pexorin.com by 13 November, 2010</p>
    </section>
    <div class="flourish" role="img" aria-label="Dark scrolling flourish ornament"></div>
  </main>
</body>
</html>
```